TAILWIND FIELDS Pet Resorts Outdoor Signage

4 x 8 outdoor signage design for our two locations

Target Market(s)

Existing and New Customers

Industry/Entity Type

Pet Care

Font styles to use
Sans Serif

Colors

Designer to choose colors to be used in the design.

```html
<!DOCTYPE html>
<html lang="en">
<head>
<meta charset="utf-8">
<title>Tailwind Fields Pet Resort – Outdoor Sign</title>
<link rel="stylesheet" href="https://fonts.googleapis.com/css2?family=Arimo:wght@400;700&family=Roboto+Condensed:wght@700&display=swap">
<style>
  :root {
    --navy: #170e3f;
    --teal: #468ea3;
    --slate: #55555a;
    --white: #ffffff;
    --page: #ffffff;
  }
  * { margin: 0; padding: 0; box-sizing: border-box; }
  html, body {
    width: 1200px; height: 999px; overflow: hidden;
    background: var(--page);
    font-family: "Arimo", Arial, sans-serif;
  }
  .sign {
    position: absolute;
    left: 370px; top: 40px;
    width: 459px; height: 918px;
    background: var(--navy);
    color: var(--white);
  }
  .brand-name {
    position: absolute;
    left: 0; right: 0; top: 120px;
    text-align: center;
    font-weight: 700;
    font-size: 64px;
    line-height: 1.05;
    letter-spacing: 1px;
    color: var(--teal);
  }
  .tagline {
    position: absolute;
    left: 0; right: 0; top: 343px;
    text-align: center;
    font-weight: 700;
    font-size: 42px;
  }
  .breed-note {
    position: absolute;
    left: 0; right: 0; top: 406px;
    text-align: center;
    font-family: "Roboto Condensed", "Arial Narrow", sans-serif;
    font-weight: 700;
    font-size: 39px;
    color: var(--teal);
    letter-spacing: 0.5px;
  }
  .services {
    position: absolute;
    left: 44px; top: 470px;
    list-style: none;
  }
  .service {
    display: flex; align-items: center;
    height: 49.7px;
    font-weight: 700;
    font-size: 26px;
  }
  .service svg { width: 34px; height: 34px; margin-right: 26px; flex: none; }
  .phone {
    position: absolute;
    left: 0; right: 0; top: 740px;
    text-align: center;
    font-weight: 700;
    font-size: 56px;
    letter-spacing: -0.5px;
  }
  .web-band {
    position: absolute;
    left: 0; right: 0; top: 818px;
    height: 55px;
    background: var(--teal);
    display: flex; align-items: center; justify-content: center;
    font-weight: 700;
    font-size: 27px;
    letter-spacing: 3.5px;
  }
</style>
</head>
<body>
<svg width="0" height="0" style="position:absolute" aria-hidden="true">
  <symbol id="bone-badge" viewBox="0 0 34 34">
    <circle cx="17" cy="17" r="17" fill="#468ea3"/>
    <rect x="10" y="15" width="14" height="4" fill="#170e3f"/>
    <circle cx="9.5" cy="14.5" r="3" fill="#170e3f"/>
    <circle cx="9.5" cy="19.5" r="3" fill="#170e3f"/>
    <circle cx="24.5" cy="14.5" r="3" fill="#170e3f"/>
    <circle cx="24.5" cy="19.5" r="3" fill="#170e3f"/>
  </symbol>
</svg>

<main class="sign">
  <div class="brand-name">TAILWIND<br>FIELDS</div>
  <div class="tagline">PET RESORT</div>
  <div class="breed-note">ALL BREED FRIENDLY</div>
  <ul class="services">
    <li class="service"><svg><use href="#bone-badge"/></svg>Boarding</li>
    <li class="service"><svg><use href="#bone-badge"/></svg>Daycare</li>
    <li class="service"><svg><use href="#bone-badge"/></svg>Training</li>
    <li class="service"><svg><use href="#bone-badge"/></svg>Full-ServiceSalon</li>
    <li class="service"><svg><use href="#bone-badge"/></svg>Pet Taxi &amp; More</li>
  </ul>
  <div class="phone">905-555-0148</div>
  <div class="web-band">www.tailwindfields.ca</div>
</main>
</body>
</html>
```